Meridian Clearsound Wellness LLC Card Design

Need business card with a logo for a hearing aid sales and audiology business. We have two Hearing Instrument Specialists and one Audiologist on staff. Over 25 years in business. Locally owned and operated. Financing available. Most insurances accepted.

Meridian Clearsound Wellness LLC
48730 W Larkfield, Suite 9
Spokane, WA 99371
509-617-2084
www.meridianclearsound-example.com

Manager
Tobias Wrenfield HIS COHC
License #81957260

Target Market(s)

50yr old + people with a hearing loss.

Industry/Entity Type

Business

Contact Information for Business Card

48730 W Larkfield, Suite 9
Spokane, WA 99371
509-617-2084
www.meridianclearsound-example.com

Manager
Tobias Wrenfield HIS COHC
RTEQ #81957260

Font styles to use
Serif
Sans Serif

Requirements
Must have
• Business name, Tobias's name and title(s) and contact information, License #, web address
Nice to have
Should not have

```html
<!DOCTYPE html>
<html lang="en">
<head>
<meta charset="utf-8">
<title>Meridian Clearsound Wellness – Business Card</title>
<link rel="stylesheet" href="https://fonts.googleapis.com/css2?family=Josefin+Slab:wght@400;600&display=swap">
<style>
  :root {
    --backdrop: #1f1f1f;
    --card-white: #f4f4f2;
    --brand-green: #95c13d;
    --ink: #2e3528;
    --ink-soft: #3f4a36;
    --name-white: #ffffff;
  }
  * { box-sizing: border-box; margin: 0; padding: 0; }
  html, body {
    width: 1200px; height: 800px; overflow: hidden;
    background: var(--backdrop);
  }
  .canvas {
    position: relative; width: 1200px; height: 800px;
    display: flex; align-items: center; justify-content: center;
  }
  .card {
    position: relative; width: 1000px; height: 572px;
    border-radius: 44px; overflow: hidden;
    background: var(--card-white);
    font-family: "Josefin Slab", Georgia, serif;
    color: var(--ink);
  }
  .card__shapes { position: absolute; inset: 0; }
  .contact {
    position: absolute; left: 70px; top: 62px; width: 470px;
  }
  .contact__name {
    font-size: 38px; font-weight: 400; color: var(--name-white);
    line-height: 1.1;
  }
  .contact__creds { font-size: 22px; color: var(--ink); margin-left: 6px; }
  .contact__role, .contact__license {
    font-size: 25px; line-height: 1.35; color: var(--ink-soft);
  }
  .contact__rule {
    border: 0; border-top: 1.5px solid var(--ink);
    width: 420px; margin: 18px 0 34px -14px;
  }
  .contact__address { font-size: 27px; line-height: 1.3; color: var(--ink); }
  .contact__lines { margin-top: 34px; }
  .contact__line {
    display: flex; align-items: center; gap: 12px;
    font-size: 27px; line-height: 1.55; color: var(--ink);
  }
  .contact__line svg { flex: none; }
  .brand {
    position: absolute; left: 640px; top: 196px; width: 320px;
    text-align: center;
  }
  .brand__dot {
    display: block; width: 96px; height: 96px; margin: 0 auto 26px;
    border-radius: 50%; background: var(--brand-green);
  }
  .brand__name {
    font-size: 27px; font-weight: 600; letter-spacing: 3px;
    text-transform: uppercase; color: var(--ink-soft); line-height: 1.3;
  }
</style>
</head>
<body>
<main class="canvas">
  <section class="card" aria-label="Business card">
    <svg class="card__shapes" width="1000" height="572" viewBox="0 0 1000 572" aria-hidden="true">
      <circle cx="-350" cy="320" r="950" fill="var(--brand-green)"/>
      <circle cx="-350" cy="320" r="970" fill="none" stroke="var(--brand-green)" stroke-width="9"/>
    </svg>

    <div class="contact">
      <p class="contact__name">Tobias Wrenfield<span class="contact__creds">HIS COHC</span></p>
      <p class="contact__role">Manager</p>
      <p class="contact__license">RTEQ #81957260</p>
      <hr class="contact__rule">
      <p class="contact__address">48730 W Larkfield, Suite 9<br>Spokane, WA 99371</p>
      <div class="contact__lines">
        <p class="contact__line">
          <svg width="26" height="26" viewBox="0 0 26 26" aria-hidden="true">
            <circle cx="13" cy="13" r="11.5" fill="none" stroke="#fff" stroke-width="1.6"/>
            <path d="M9.5 7.5c-1 1-1 3 .8 5.6 1.8 2.6 3.8 3.8 5.2 3.6l1.4-1.6-2.2-1.8-1.1.8c-.9-.5-1.9-1.8-2.3-2.8l.9-1-1.4-2.5z" fill="#fff"/>
          </svg>
          509-617-2084
        </p>
        <p class="contact__line">
          <svg width="26" height="26" viewBox="0 0 26 26" aria-hidden="true">
            <circle cx="13" cy="13" r="11.5" fill="none" stroke="#fff" stroke-width="1.6"/>
            <ellipse cx="13" cy="13" rx="5" ry="11.5" fill="none" stroke="#fff" stroke-width="1.4"/>
            <path d="M2 13h22M4 7.5h18M4 18.5h18" stroke="#fff" stroke-width="1.4"/>
          </svg>
          www.meridianclearsound-example.com
        </p>
      </div>
    </div>

    <div class="brand">
      <span class="brand__dot" aria-hidden="true"></span>
      <p class="brand__name">Meridian Clearsound<br>Wellness</p>
    </div>
  </section>
</main>
</body>
</html>
```